Banner for real estate email blast

I need a banner created that will be used in a commercial real estate broadcast email headed. The banner size should be 800x129 pixels and in a JPG format. I will include our company logo and samples of some other company documents.
The banner MUST include (1) the company name, Holloway-Brisk Real Estate and (2) the following contact information:
472 Tindale Orchard Rd
Fayetteville, NC 28917
(910) 555-0143
www.HollowayBriskRE.example
Target Market(s)
Real estate agents.
Industry/Entity Type
Real Estate
Requirements
Must have
- 1. Company name
- 2. Contact info to include address, phone number, web address
- 3. Use the same green colors as in our other attached documents.
- 4. MUST be 800x129 pixels
Should not have
- Any other text other than what is mentioned in the "Must Haves"

```html
<!DOCTYPE html>
<html lang="en">
<head>
<meta charset="utf-8">
<title>Holloway-Brisk Real Estate — Email Banner</title>
<link rel="stylesheet" href="https://fonts.googleapis.com/css2?family=Cormorant+Garamond:wght@500&family=Arimo:wght@400&display=swap">
<style>
  :root {
    --green-deep: #123a1c;
    --green-main: #1d5129;
    --green-light: #2c6a39;
    --text-light: #ffffff;
    --photo-sky: #8a7a6e;
    --photo-brick: #7b4a35;
    --photo-shade: #3c3028;
  }
  html, body {
    margin: 0;
    padding: 0;
    overflow: hidden;
    background: #ffffff;
  }
  .banner {
    position: relative;
    width: 1200px;
    height: 194px;
    overflow: hidden;
    background: linear-gradient(180deg, var(--green-main) 0%, var(--green-deep) 100%);
    font-family: "Arimo", Arial, sans-serif;
    color: var(--text-light);
  }
  .banner__scene {
    position: absolute;
    inset: 0;
  }
  .brand {
    position: absolute;
    left: 8px;
    top: 6px;
    display: flex;
    align-items: center;
    gap: 14px;
  }
  .brand__mark {
    width: 92px;
    height: 92px;
    border-radius: 50%;
    background: var(--green-light);
    border: 3px solid var(--text-light);
    box-sizing: border-box;
  }
  .brand__name {
    margin: 0;
    font-family: "Cormorant Garamond", "Times New Roman", serif;
    font-weight: 500;
    color: var(--text-light);
    line-height: 1;
  }
  .brand__primary {
    display: block;
    font-size: 50px;
    letter-spacing: 0.5px;
  }
  .brand__secondary {
    display: block;
    margin-top: 4px;
    font-size: 25px;
    letter-spacing: 8px;
    text-transform: uppercase;
    padding-left: 34px;
  }
  .contact {
    position: absolute;
    left: 868px;
    top: 2px;
    margin: 0;
    font-style: normal;
    font-size: 18px;
    line-height: 23px;
    text-shadow: 0 1px 2px rgba(0,0,0,0.5);
  }
  .contact__line { display: block; }
  .contact__line--indent { padding-left: 78px; }
  .contact__line--tel { padding-left: 50px; }
  .website {
    position: absolute;
    left: 54px;
    top: 158px;
    font-size: 18px;
    color: var(--text-light);
    text-decoration: none;
  }
</style>
</head>
<body>
  <div class="banner">
    <svg class="banner__scene" width="1200" height="194" viewBox="0 0 1200 194" aria-hidden="false">
      <defs>
        <linearGradient id="photoTone" x1="0" y1="0" x2="1" y2="1">
          <stop offset="0" stop-color="var(--photo-sky)"/>
          <stop offset="0.45" stop-color="var(--photo-brick)"/>
          <stop offset="1" stop-color="var(--photo-shade)"/>
        </linearGradient>
      </defs>
      <path role="img" aria-label="Photograph of modern brick apartment buildings with balconies"
            d="M0,110 C180,112 380,86 560,66 C700,56 900,58 1200,56 L1200,194 L340,194 C300,176 230,168 0,166 Z"
            fill="url(#photoTone)"/>
      <path d="M0,166 C230,168 300,176 340,194 L0,194 Z" fill="var(--green-deep)"/>
      <path d="M0,110 C180,112 380,86 560,66 C700,56 900,58 1200,56" fill="none" stroke="var(--green-light)" stroke-width="3"/>
    </svg>

    <div class="brand">
      <span class="brand__mark"></span>
      <h1 class="brand__name">
        <span class="brand__primary">Holloway-Brisk</span>
        <span class="brand__secondary">Real Estate</span>
      </h1>
    </div>

    <address class="contact">
      <span class="contact__line">Address: 472 Tindale Orchard Rd</span>
      <span class="contact__line contact__line--indent">Fayetteville, NC 28917</span>
      <span class="contact__line contact__line--tel">Tel: (910) 555-0143</span>
    </address>

    <a class="website" href="#">www.HollowayBriskRE.example</a>
  </div>
</body>
</html>
```